Women's Health Company needs business card

We need a business card for a USA based women's health care company. We use digital technology to enhance therapy prescribed by clinicians for their patients

```html
<!DOCTYPE html>
<html lang="en">
<head>
<meta charset="utf-8">
<title>Velora Health — Business Card</title>
<link rel="stylesheet" href="https://fonts.googleapis.com/css2?family=Montserrat:wght@400;500&display=swap">
<style>
  :root {
    --backdrop: #2b2b31;
    --teal: #76c0bc;
    --teal-raised: #86cdc9;
    --purple: #8e4fae;
    --ink: #6b6b6b;
    --paper: #ffffff;
  }
  * { margin: 0; padding: 0; box-sizing: border-box; }
  html, body { width: 1200px; height: 817px; overflow: hidden; }
  body {
    background: var(--backdrop);
    font-family: "Montserrat", sans-serif;
    position: relative;
  }
  .card {
    position: absolute;
    width: 525px;
    height: 300px;
    border-radius: 30px;
    box-shadow: 0 14px 30px rgba(0,0,0,0.45);
    overflow: hidden;
  }
  .card-front {
    left: 50px;
    top: 258px;
    background: var(--teal);
    display: flex;
    align-items: center;
    justify-content: center;
  }
  .card-back {
    left: 625px;
    top: 258px;
    background: var(--paper);
  }
  .wordmark {
    display: flex;
    align-items: center;
    gap: 10px;
    font-weight: 500;
    font-size: 40px;
    letter-spacing: 1px;
    white-space: nowrap;
  }
  .wordmark-dot {
    width: 12px;
    height: 12px;
    border-radius: 50%;
  }
  .card-front .wordmark { color: var(--teal-raised); }
  .card-front .wordmark-dot { background: var(--teal-raised); }
  .card-back .wordmark {
    position: absolute;
    left: 36px;
    top: 128px;
    font-size: 30px;
    color: var(--teal);
  }
  .card-back .wordmark-dot { background: var(--purple); width: 10px; height: 10px; }
  .divider {
    position: absolute;
    left: 300px;
    top: 0;
    width: 2px;
    height: 100%;
    background: var(--purple);
  }
  .details {
    position: absolute;
    left: 328px;
    top: 46px;
    color: var(--ink);
  }
  .person-name {
    color: var(--teal);
    font-weight: 500;
    font-size: 21px;
    letter-spacing: 0.5px;
    text-transform: uppercase;
  }
  .person-role {
    font-size: 14px;
    margin-top: 2px;
  }
  .address {
    font-size: 12px;
    line-height: 1.5;
    margin-top: 22px;
  }
  .contact-list {
    list-style: none;
    font-size: 12px;
    line-height: 22px;
    margin-top: 12px;
  }
  .icon-rail {
    position: absolute;
    left: 288px;
    top: 174px;
    width: 26px;
    height: 70px;
    border-radius: 6px;
    background: var(--purple);
    display: flex;
    flex-direction: column;
    align-items: center;
    justify-content: space-around;
    padding: 4px 0;
  }
  .icon-rail svg { width: 13px; height: 13px; display: block; }
</style>
</head>
<body>
  <section class="card card-front" aria-label="Card front">
    <div class="wordmark"><span class="wordmark-dot"></span>Velora Health</div>
  </section>

  <section class="card card-back" aria-label="Card back">
    <div class="wordmark"><span class="wordmark-dot"></span>Velora Health</div>
    <div class="divider"></div>

    <div class="icon-rail" aria-hidden="true">
      <svg viewBox="0 0 24 24"><path fill="#fff" d="M6.6 10.8a15.2 15.2 0 0 0 6.6 6.6l2.2-2.2c.3-.3.7-.4 1-.2 1.1.4 2.3.6 3.6.6.6 0 1 .4 1 1V20c0 .6-.4 1-1 1A17 17 0 0 1 3 4c0-.6.4-1 1-1h3.5c.6 0 1 .4 1 1 0 1.3.2 2.5.6 3.6.1.3 0 .7-.2 1z"/></svg>
      <svg viewBox="0 0 24 24"><rect x="2" y="5" width="20" height="14" rx="2" fill="#fff"/><path d="M3 6l9 7 9-7" stroke="#8e4fae" stroke-width="2" fill="none"/></svg>
      <svg viewBox="0 0 24 24" fill="none" stroke="#fff" stroke-width="2"><circle cx="12" cy="12" r="9"/><path d="M3 12h18M12 3c3 3 3 15 0 18M12 3c-3 3-3 15 0 18"/></svg>
    </div>

    <div class="details">
      <p class="person-name">Dana Ellis</p>
      <p class="person-role">Manager</p>
      <p class="address">412 Willow Bend Road<br>Boise Idaho 83702</p>
      <ul class="contact-list">
        <li>555-014-2290</li>
        <li>hello@velorahealth.com</li>
        <li>www.velorahealth.com</li>
      </ul>
    </div>
  </section>
</body>
</html>
```